Private chef located in Vail, CO

I would like my info located at the top of the landing page, perhaps some Vail mountain landscapes that I could swap out from summer to winter photos. I need the menu bar to have a link to a blog, about me, photo gallery, recipes & beer reviews. I would also like to have a shop, but only populated with products from quolex or other online retailers that I can affiliate with.
Target Market(s)
Extremely wealthy, affluent people, concierge, international
Number of Pages Required
5+ page

```html
<!DOCTYPE html>
<html lang="en">
<head>
<meta charset="utf-8">
<title>Private Chef – Vail Mountains</title>
<link rel="stylesheet" href="https://fonts.googleapis.com/css2?family=Bodoni+Moda:wght@400;500&family=Open+Sans:wght@400;600&display=swap">
<style>
  :root {
    --sky-deep: #1d4770;
    --sky-mid: #5f86ad;
    --snow: #dfe7ef;
    --snow-shadow: #9fb3c6;
    --frame: rgba(48, 48, 50, 0.78);
    --frame-edge: #1e1e1e;
    --panel: rgba(14, 14, 14, 0.86);
    --panel-soft: rgba(18, 18, 18, 0.62);
    --text-light: #ffffff;
    --text-muted: #a9a9a9;
    --field-line: #bdbdbd;
  }
  * { margin: 0; padding: 0; box-sizing: border-box; }
  html, body { width: 1200px; height: 2579px; overflow: hidden; background: #1a1a1a; }
  body { position: relative; font-family: "Open Sans", Arial, sans-serif; color: var(--text-light); }

  .screen { position: absolute; left: 0; width: 1200px; overflow: hidden; }
  .screen--home { top: 0; height: 860px; }
  .screen--about { top: 860px; height: 860px; }
  .screen--contact { top: 1720px; height: 859px; }

  .landscape {
    position: absolute; inset: 0;
    background:
      radial-gradient(ellipse 60% 40% at 85% 35%, rgba(240,244,248,0.9), transparent 70%),
      linear-gradient(180deg, var(--sky-deep) 0%, var(--sky-mid) 30%, var(--snow) 55%, var(--snow-shadow) 78%, var(--snow) 100%);
  }

  .frame {
    position: absolute; left: 60px; width: 1077px;
    background: var(--frame); border: 3px solid var(--frame-edge);
  }
  .screen--home .frame { top: 57px; height: 745px; }
  .screen--about .frame { top: 60px; height: 758px; }
  .screen--contact .frame { top: 48px; height: 772px; }

  .main-nav { position: absolute; top: 22px; left: 48px; display: flex; gap: 0; }
  .screen--contact .main-nav { left: 26px; }
  .main-nav a {
    color: var(--text-light); text-decoration: none; font-size: 11px;
    letter-spacing: 0.2px; margin-right: 33px; position: relative; padding-bottom: 6px;
  }
  .main-nav a.is-active::after {
    content: ""; position: absolute; left: 0; bottom: 0; width: 18px; height: 1px; background: var(--text-light);
  }

  .display { font-family: "Bodoni Moda", "Didot", serif; font-weight: 400; text-transform: uppercase; letter-spacing: 1px; }

  .hero-title {
    position: absolute; left: 113px; top: 262px; width: 497px; height: 103px;
    background: var(--panel); display: flex; align-items: center; justify-content: center;
    font-size: 56px;
  }
  .location-badge {
    position: absolute; left: 811px; top: 555px; width: 272px; height: 115px;
    background: var(--panel-soft); text-align: center; padding-top: 22px;
  }
  .location-badge__label { font-size: 16px; }
  .location-badge__place { font-family: "Bodoni Moda", serif; font-size: 32px; margin-top: 4px; }

  .panel { position: absolute; left: 113px; width: 970px; background: var(--panel); text-align: center; }
  .screen--about .panel { top: 226px; height: 504px; }
  .screen--contact .panel { top: 231px; height: 498px; background: rgba(40,40,42,0.72); }
  .panel__title { font-size: 56px; margin-top: 50px; }

  .about-text {
    width: 670px; margin: 56px auto 0; font-size: 18px; line-height: 39px; color: var(--text-muted);
  }

  .contact-form { position: absolute; left: 55px; top: 150px; width: 338px; }
  .field {
    display: block; width: 338px; height: 41px; border: 1px solid var(--field-line);
    padding: 10px 14px; font-size: 13px; color: var(--text-muted); text-align: left; margin-bottom: 24px;
  }
  .field--message { height: 101px; }
  .send-button {
    position: absolute; right: 0; top: 272px; display: flex; align-items: center; gap: 14px;
    font-size: 13px; color: var(--text-light);
  }

  .contact-details { position: absolute; left: 500px; top: 160px; width: 402px; text-align: center; font-size: 13px; }
  .contact-details__phone { margin-bottom: 46px; }
  .contact-details__location { margin-bottom: 46px; }
  .contact-details__location span { color: var(--text-muted); }
  .contact-details__follow { font-size: 15px; color: var(--text-muted); margin-bottom: 18px; }
  .social-links { display: flex; justify-content: center; gap: 26px; font-size: 14px; font-weight: 600; }
</style>
</head>
<body>

<section class="screen screen--home">
  <div class="landscape" role="img" aria-label="Winter landscape of snowy Vail mountain slopes under a blue sky"></div>
  <div class="frame">
    <nav class="main-nav">
      <a class="is-active">HOME</a><a>ABOUT</a><a>PHOTO GALLERY</a><a>RECIPES</a><a>BEER REVIEWS</a><a>BLOG</a>
    </nav>
  </div>
  <h1 class="hero-title display">Private Chef</h1>
  <div class="location-badge">
    <p class="location-badge__label">Located in:</p>
    <p class="location-badge__place">Vail Mountains</p>
  </div>
</section>

<section class="screen screen--about">
  <div class="landscape" role="img" aria-label="Snow-covered mountain valley in winter"></div>
  <div class="frame">
    <nav class="main-nav">
      <a class="is-active">HOME</a><a>ABOUT</a><a>PHOTO GALLERY</a><a>RECIPES</a><a>BEER REVIEWS</a><a>BLOG</a>
    </nav>
  </div>
  <div class="panel">
    <h2 class="panel__title display">About Me</h2>
    <p class="about-text">Lorem ipsum dolor sit amet, consectetur adipiscing elit, sed do eiusmod tempor incididunt ut labore et dolore magna aliqua. Ut enim ad minim veniam, quis nostrud exercitation ullamco laboris nisi ut aliquip ex ea commodo consequat. Duis aute irure dolor in reprehenderit in volupta-te velit esse cillum dolore eu fugiat nulla pariatur.</p>
  </div>
</section>

<section class="screen screen--contact">
  <div class="landscape" role="img" aria-label="Snowy mountain ridge under a cloudy winter sky"></div>
  <div class="frame">
    <nav class="main-nav">
      <a class="is-active">HOME</a><a>ABOUT</a><a>PHOTO GALLERY</a><a>RECIPES</a><a>BEER REVIEWS</a><a>BLOG</a>
    </nav>
  </div>
  <div class="panel">
    <h2 class="panel__title display">Contact</h2>
    <div class="contact-form">
      <div class="field">Name</div>
      <div class="field">Email</div>
      <div class="field field--message">Write message...</div>
      <div class="send-button">Send message
        <svg width="34" height="14" viewBox="0 0 34 14" aria-hidden="true"><path d="M0 7H32M25 1L32 7L25 13" fill="none" stroke="#fff" stroke-width="1.3"/></svg>
      </div>
    </div>
    <div class="contact-details">
      <p class="contact-details__phone">+1 (970) 555 0142</p>
      <p class="contact-details__location"><span>Location:</span> Vail Mountains, CO</p>
      <p class="contact-details__follow">Follow:</p>
      <div class="social-links"><span>Snapvue</span><span>Chirpline</span><span>Friendsy</span></div>
    </div>
  </div>
</section>

</body>
</html>
```